Updated Business Card for Optometry Practice

We're a growing optometry practice that is moving to a beautiful new office and we want to update our business card. We just updated our logo so the new card should reflect the new logo. Our practice continually invests in state of the art instruments to help us provide eye care that is thorough, comfortable, efficient and educational.

I've attached our current card and logo. You can reference this for the information I would like on the card. The tag line on the back is "We're changing the way you see."

Upon completion of this project we will need (amongst other formats) Photoshop files of the card so I can change employee names to print cards for each employee.

```html
<!DOCTYPE html>
<html lang="en">
<head>
<meta charset="utf-8">
<title>Brightwater Family Eyecare – Business Card</title>
<link rel="stylesheet" href="https://fonts.googleapis.com/css2?family=Montserrat:wght@400;500;700;800&family=Open+Sans:wght@400;600&display=swap">
<style>
  :root {
    --backdrop: #1c1c1e;
    --gold: #d5b032;
    --navy: #14284e;
    --white: #ffffff;
    --ink: #14284e;
  }
  * { box-sizing: border-box; margin: 0; padding: 0; }
  html, body {
    width: 1200px; height: 1200px; overflow: hidden;
    background: var(--backdrop);
  }
  .canvas {
    position: relative; width: 1200px; height: 1200px;
    font-family: "Montserrat", sans-serif;
  }
  .card {
    position: absolute; left: 150px; width: 900px; height: 514px;
    box-shadow: 0 10px 30px rgba(0,0,0,.45);
    overflow: hidden;
  }
  .brand-row {
    position: absolute; display: flex; align-items: center; white-space: nowrap;
  }
  .brand-name {
    font-family: "Open Sans", sans-serif; font-weight: 400; line-height: 1;
  }
  .brand-dot { border-radius: 50%; flex: none; }
  .brand-sub {
    font-family: "Open Sans", sans-serif; font-weight: 400;
    letter-spacing: .32em; white-space: nowrap;
  }
  /* Front */
  .card--front { top: 60px; background: var(--gold); }
  .card--front .brand-row { left: 196px; top: 122px; gap: 40px; }
  .card--front .brand-name { font-size: 88px; color: var(--navy); }
  .card--front .brand-dot { width: 46px; height: 46px; background: var(--white); }
  .band {
    position: absolute; left: 170px; top: 245px; width: 620px; height: 54px;
    background: var(--navy);
    display: flex; align-items: center; padding-left: 38px;
  }
  .band .brand-sub { color: var(--white); font-size: 34px; }
  .tagline {
    position: absolute; left: 0; right: 0; top: 372px; text-align: center;
    color: var(--white); font-weight: 700; font-size: 17px; letter-spacing: .02em;
  }
  /* Back */
  .card--back { top: 626px; display: flex; }
  .contact-side {
    position: relative; width: 420px; height: 100%;
    background: var(--white); color: var(--ink);
    padding: 58px 0 0 56px;
  }
  .person-name { font-weight: 800; font-size: 27px; }
  .person-role { font-weight: 400; font-size: 17px; margin-top: 2px; }
  .address { margin-top: 118px; font-size: 19px; line-height: 1.3; }
  .contact-list { list-style: none; margin-top: 34px; }
  .contact-list li {
    display: flex; align-items: center; gap: 14px;
    font-size: 19px; margin-bottom: 14px;
  }
  .contact-list svg { width: 20px; height: 20px; flex: none; fill: var(--ink); }
  .brand-side {
    position: relative; flex: 1; background: var(--navy);
  }
  .brand-side .brand-row { left: 50px; top: 190px; gap: 22px; }
  .brand-side .brand-name { font-size: 60px; color: var(--white); }
  .brand-side .brand-dot { width: 36px; height: 36px; background: var(--gold); }
  .brand-side .brand-sub {
    position: absolute; left: 54px; top: 276px;
    font-size: 27px; color: var(--white);
  }
</style>
</head>
<body>
<main class="canvas">
  <section class="card card--front" aria-label="Card front">
    <div class="brand-row">
      <div class="brand-name">Brightwater</div>
      <div class="brand-dot" aria-hidden="true"></div>
    </div>
    <div class="band"><span class="brand-sub">Family Eyecare</span></div>
    <p class="tagline">We're changing the way you see</p>
  </section>

  <section class="card card--back" aria-label="Card back">
    <div class="contact-side">
      <h1 class="person-name">Daniel Marsh, OD</h1>
      <p class="person-role">Optometrist</p>
      <p class="address">2870 Meadow Ridge Blvd<br>Fairview,&nbsp; MO 63100</p>
      <ul class="contact-list">
        <li>
          <svg viewBox="0 0 24 24" aria-hidden="true"><path d="M6.6 10.8a15.1 15.1 0 0 0 6.6 6.6l2.2-2.2c.3-.3.7-.4 1-.2 1.1.4 2.3.6 3.6.6.6 0 1 .4 1 1V20c0 .6-.4 1-1 1A17 17 0 0 1 3 4c0-.6.4-1 1-1h3.5c.6 0 1 .4 1 1 0 1.3.2 2.5.6 3.6.1.3 0 .7-.2 1z"/></svg>
          <span>(555) 201-3847</span>
        </li>
        <li>
          <svg viewBox="0 0 24 24" aria-hidden="true"><path d="M2 5h20v14H2z M2 5l10 8 10-8" fill="none" stroke="#14284e" stroke-width="2"/><path d="M2 5h20l-10 8z"/></svg>
          <span>dan@brightwatereyecare.com</span>
        </li>
        <li>
          <svg viewBox="0 0 24 24" aria-hidden="true"><circle cx="12" cy="12" r="9" fill="none" stroke="#14284e" stroke-width="2"/><path d="M3 12h18M12 3c3 3 3 15 0 18M12 3c-3 3-3 15 0 18" fill="none" stroke="#14284e" stroke-width="1.6"/></svg>
          <span>dan@brightwatereyecare.com</span>
        </li>
      </ul>
    </div>
    <div class="brand-side">
      <div class="brand-row">
        <div class="brand-name">Brightwater</div>
        <div class="brand-dot" aria-hidden="true"></div>
      </div>
      <div class="brand-sub">Family Eyecare</div>
    </div>
  </section>
</main>
</body>
</html>
```